Create for us a Shop-Stopper Business Card

We need a standout, first class business card to go along with our new brand strategy. Sleek, Contemporary and fresh.

Colors and theme must sync with our websitewww.pelvorpower.co.uk

We want a business card that has a global brand appeal. TKR Energy is a small UK renewable company that specialises in energy projects in Africa. We want a business card that has the following characteristics: Very short, precise, global, stand out, NOT TOO LOUD but contemporary. The company's colour themes are White, Grey with a hint of green.

Target Market(s)

Business exec, high net worth individuals, investors, commercial leaders, suppliers, government officials

Industry/Entity Type

Solar Energy

Contact Information for Business Card

Logo, Name, Title, Address, web address, email,

Requirements
Must have
• Logo must be sharp
Nice to have
• Adapt fonts from the logo. The large circular side of the logo at the back in a very refreshing way
Should not have
• No solar panel shapes or image.Very little black. If possible avoid black. Its not coming out nice. I think !!!

```html
<!DOCTYPE html>
<html lang="en">
<head>
<meta charset="utf-8">
<title>TKR Energy – Business Card</title>
<link rel="stylesheet" href="https://fonts.googleapis.com/css2?family=Source+Sans+3:wght@400;600&display=swap">
<style>
  :root {
    --bg: #4a4a4a;
    --white: #ffffff;
    --green-dark: #137434;
    --green-mid: #0a8249;
    --green-light: #8dc63f;
    --yellow: #e8e81e;
    --yellow-bright: #f4f21a;
    --ink: #333333;
    --grey: #5e5e5e;
  }
  html, body {
    margin: 0;
    padding: 0;
    width: 1200px;
    height: 1200px;
    overflow: hidden;
    background: var(--bg);
    font-family: "Source Sans 3", "Myriad Pro", Arial, sans-serif;
  }
  .canvas {
    position: relative;
    width: 1200px;
    height: 1200px;
  }
  .card {
    position: absolute;
    left: 271px;
    width: 659px;
    height: 372px;
    overflow: hidden;
    box-shadow: 0 6px 14px rgba(0,0,0,0.35);
  }
  .card-front { top: 166px; background: var(--white); }
  .card-back {
    top: 638px;
    background: linear-gradient(90deg, var(--green-light) 0%, #6db342 25%, #3e9a47 45%, var(--green-mid) 65%, var(--green-mid) 100%);
  }
  .swoosh { position: absolute; left: 0; top: 0; }

  .brand {
    position: absolute;
    display: flex;
    align-items: center;
    gap: 14px;
  }
  .brand-front { left: 200px; top: 90px; }
  .brand-dot {
    width: 80px;
    height: 80px;
    border-radius: 50%;
    background: var(--green-dark);
  }
  .brand-name {
    font-weight: 600;
    font-size: 52px;
    letter-spacing: 1px;
    line-height: 1;
  }
  .brand-front .brand-name { color: var(--grey); }
  .brand-back { left: 359px; top: 160px; }
  .brand-back .brand-name { color: var(--yellow-bright); font-size: 50px; }

  .person { position: absolute; left: 30px; top: 230px; }
  .person-name {
    margin: 0;
    font-weight: 400;
    font-size: 25px;
    color: var(--green-dark);
    line-height: 1.1;
  }
  .person-title {
    margin: 2px 0 0;
    font-size: 17px;
    color: var(--ink);
  }
  .contact {
    list-style: none;
    margin: 18px 0 0;
    padding: 0;
    font-size: 17px;
    color: var(--ink);
  }
  .contact li {
    display: flex;
    align-items: center;
    gap: 10px;
    line-height: 23px;
  }
  .contact svg { width: 16px; height: 14px; }

  .web {
    position: absolute;
    color: var(--white);
    font-size: 17px;
  }
  .card-front .web { right: 55px; bottom: 20px; }
  .card-back .web { right: 29px; bottom: 28px; }

  .emblem-area {
    position: absolute;
    left: 0;
    top: 120px;
    width: 370px;
    height: 252px;
    border-radius: 185px 185px 0 0;
    background: radial-gradient(ellipse at 50% 60%, #8cc63f 0%, #5fae44 45%, rgba(19,116,52,0.9) 75%, rgba(19,116,52,0) 100%);
  }
</style>
</head>
<body>
<main class="canvas">

  <section class="card card-front" aria-label="Business card front">
    <svg class="swoosh" width="659" height="372" viewBox="0 0 659 372" aria-hidden="true">
      <defs>
        <linearGradient id="topEdge" x1="0" x2="1" y1="0" y2="0">
          <stop offset="0" stop-color="#e8ec24"/>
          <stop offset="1" stop-color="#8dc63f"/>
        </linearGradient>
        <linearGradient id="bottomEdge" x1="0" x2="1" y1="0" y2="0">
          <stop offset="0" stop-color="#8dc63f"/>
          <stop offset="1" stop-color="#f0ee1c"/>
        </linearGradient>
      </defs>
      <path d="M0 40 C120 80 260 90 372 0 L0 0 Z" fill="url(#topEdge)" transform="translate(0,30)"/>
      <path d="M0 0 L372 0 C300 60 180 80 0 55 Z" fill="var(--green-dark)"/>
      <path d="M285 372 C400 300 560 290 659 320 L659 372 Z" fill="url(#bottomEdge)" transform="translate(0,-22)"/>
      <path d="M285 372 C400 320 560 300 659 332 L659 372 Z" fill="var(--green-dark)"/>
    </svg>

    <div class="brand brand-front">
      <span class="brand-dot"></span>
      <span class="brand-name">TKR ENERGY</span>
    </div>

    <div class="person">
      <h1 class="person-name">Daniel Hartley</h1>
      <p class="person-title">Managing Partner</p>
      <ul class="contact">
        <li>
          <svg viewBox="0 0 16 14" aria-hidden="true"><path d="M1 5 C1 1 15 1 15 5 L12 6 L11 4 L5 4 L4 6 Z M4 7 L12 7 L14 13 L2 13 Z" fill="var(--green-dark)"/></svg>
          (00) 000-0000
        </li>
        <li>
          <svg viewBox="0 0 16 14" aria-hidden="true"><rect x="1" y="2" width="14" height="10" fill="var(--green-dark)"/><path d="M1 2 L8 8 L15 2" stroke="#fff" stroke-width="1.2" fill="none"/></svg>
          dhartley@pelvorpower.co.uk
        </li>
      </ul>
    </div>

    <span class="web">www.pelvorpower.co.uk</span>
  </section>

  <section class="card card-back" aria-label="Business card back">
    <div class="emblem-area" role="img" aria-label="Large brand emblem decoration in greens and yellow"></div>
    <div class="brand brand-back">
      <span class="brand-name">TKR ENERGY</span>
    </div>
    <span class="web">www.pelvorpower.co.uk</span>
  </section>

</main>
</body>
</html>
```